Super Greens Label for Supplement Bottle

We want to design a front label for a health supplement bottle. The product is called Meadow Twist Chews™. This will be a new product so there is no current website for the product. The focus is on supergreens that taste great and deliver support for energy, digestion, and immune defense.
We want it to be modern, vibrant and appealing.
Bottle size: standard size supplement CLEAR bottle size, with white child resistant cap and the label panel dimensions are 3” x 7”. The label should be primarily white and green, with a touch of red; (see color palettes)/it can also ONLY be white and green. See samples attached.
We are only focused on the front of the bottle design, not on the back, but leave space for the supplement panel and other text on the back.
So the text for the front of the bottle is:
RT Balden's
Meadow Twist Chews™
Super Greens Blend for:
Energy, Digestion, and Immune Support*
60 Gummies | Dietary Supplement
Raspberry Flavor Gummies
Off to side of the label:
Non-GMO
Vegan Friendly
Plant-Based
Gelatin Free
Colors
Designer to choose colors to be used in the design.

```html
<!DOCTYPE html>
<html lang="en">
<head>
<meta charset="UTF-8">
<title>Meadow Twist Chews™ Front Label</title>
<link rel="stylesheet" href="https://fonts.googleapis.com/css2?family=Poppins:wght@500;600&family=DM+Sans:wght@400;500;700&family=Barlow+Semi+Condensed:wght@400;500&display=swap">
<style>
  :root {
    --page: #eeeeef;
    --label-white: #ffffff;
    --green: #0f9a78;
    --green-deep: #02714f;
    --green-light: #1aa88a;
    --red: #e6374f;
    --red-deep: #e0121f;
    --grey-band: #e6e7e9;
    --ink: #2f3a3a;
    --ink-soft: #5c6666;
    --icon-line: #2f9b80;
  }
  * { box-sizing: border-box; margin: 0; padding: 0; }
  html, body { width: 1200px; height: 1200px; overflow: hidden; }
  body { background: var(--page); position: relative; font-family: "DM Sans", sans-serif; }

  .label {
    position: absolute; left: 100px; top: 46px;
    width: 1000px; height: 1108px;
    background: var(--label-white);
    overflow: hidden;
    box-shadow: 0 6px 24px rgba(0,0,0,0.08);
  }

  .brand-pill {
    position: absolute; left: 248px; top: 94px;
    width: 299px; height: 64px;
    border: 2px solid var(--green-deep); border-radius: 32px;
    display: flex; align-items: center; justify-content: center;
    font-family: "DM Sans", sans-serif; font-weight: 500;
    font-size: 34px; letter-spacing: 4px; color: var(--green-deep);
  }

  .title-band {
    position: absolute; left: 0; top: 240px; width: 1000px; height: 351px;
    background: linear-gradient(100deg, var(--green) 0%, var(--green-light) 45%, var(--green-deep) 100%);
  }
  .product-name {
    position: absolute; left: 54px; top: 56px;
    font-family: "Poppins", sans-serif; font-weight: 600;
    font-size: 108px; line-height: 124px; color: #fff; letter-spacing: -1px;
  }

  .flavor-band {
    position: absolute; left: 0; top: 591px; width: 1000px; height: 56px;
    background: linear-gradient(90deg, var(--red) 0%, var(--red-deep) 100%);
  }
  .flavor-text {
    position: absolute; left: 59px; top: 0; line-height: 56px;
    font-family: "DM Sans", sans-serif; font-weight: 700;
    font-size: 30px; letter-spacing: 7px; color: #fff;
  }

  .fruit-art {
    position: absolute; left: 499px; top: 462px; width: 270px; height: 200px;
    border-radius: 50% 45% 50% 40%;
    background: radial-gradient(circle at 55% 60%, #d9243f 0%, #e8566a 55%, #5aa64a 100%);
  }

  .claims-band {
    position: absolute; left: 0; top: 647px; width: 1000px; height: 121px;
    background: linear-gradient(90deg, #f3f3f4 0%, var(--grey-band) 60%, #cfd1d3 100%);
  }
  .claim {
    position: absolute; top: 22px; width: 140px; margin-left: -70px;
    text-align: center; color: var(--ink-soft);
    font-family: "DM Sans", sans-serif; font-size: 14px;
  }
  .claim svg { display: block; margin: 0 auto 6px; }
  .claim-nongmo { left: 79px; }
  .claim-plant { left: 185px; }
  .claim-vegan { left: 339px; }
  .claim-gelatin { left: 516px; }

  .count-badge {
    position: absolute; left: 722px; top: 630px; width: 88px; height: 126px;
    background: var(--green); border-radius: 4px;
    color: #fff; text-align: center; font-family: "DM Sans", sans-serif;
  }
  .count-number { display: block; font-size: 62px; font-weight: 400; line-height: 66px; margin-top: 20px; letter-spacing: -2px; }
  .count-unit { display: block; font-size: 15px; }

  .benefits {
    position: absolute; left: 59px; top: 828px;
    font-family: "Barlow Semi Condensed", sans-serif; color: var(--ink);
  }
  .benefits-heading { font-size: 31px; font-weight: 500; margin-bottom: 8px; }
  .benefits-list { list-style: none; }
  .benefits-list li { font-size: 31px; line-height: 49px; display: flex; align-items: center; gap: 8px; }

  .greens-art {
    position: absolute; left: 331px; top: 773px; width: 546px; height: 300px;
    background:
      radial-gradient(ellipse 40% 45% at 72% 35%, #b7cf7e 0%, #c89257 60%, transparent 62%),
      radial-gradient(ellipse 45% 35% at 35% 75%, #4f8a2a 0%, #7bb045 60%, transparent 62%);
  }

  .footer-strip {
    position: absolute; left: 0; top: 1066px; width: 1000px; height: 42px;
    background: linear-gradient(180deg, #ffffff 0%, #eceded 100%);
  }
  .footer-text {
    position: absolute; left: 59px; top: 10px;
    font-family: "DM Sans", sans-serif; font-size: 14px; font-weight: 500;
    letter-spacing: 7px; color: var(--ink);
  }
</style>
</head>
<body>
  <main class="label">
    <div class="brand-pill">RT BALDEN'S</div>

    <section class="title-band">
      <h1 class="product-name">Meadow Twist<br>Chews™</h1>
    </section>

    <section class="flavor-band">
      <span class="flavor-text">RASPBERRY FLAVOR</span>
    </section>

    <div class="fruit-art" role="img" aria-label="Photo of fresh raspberries with a green mint leaf"></div>

    <section class="claims-band">
      <div class="claim claim-nongmo">
        <svg width="40" height="40" viewBox="0 0 40 40"><circle cx="20" cy="20" r="17" fill="none" stroke="var(--icon-line)" stroke-width="1.5"/><line x1="9" y1="31" x2="31" y2="9" stroke="var(--icon-line)" stroke-width="1.5"/></svg>
        Non-GMO
      </div>
      <div class="claim claim-plant">
        <svg width="40" height="40" viewBox="0 0 40 40"><circle cx="20" cy="20" r="17" fill="none" stroke="var(--icon-line)" stroke-width="1.5"/><path d="M20 30 V18 M20 22 C14 22 12 17 13 13 C18 13 20 17 20 22 M20 20 C25 20 27 15 26 11 C21 11 20 15 20 20" fill="none" stroke="var(--icon-line)" stroke-width="1.5"/></svg>
        Plant-Based
      </div>
      <div class="claim claim-vegan">
        <svg width="40" height="40" viewBox="0 0 40 40"><circle cx="20" cy="20" r="17" fill="none" stroke="var(--icon-line)" stroke-width="1.5"/><rect x="9" y="16" width="22" height="8" rx="2" fill="none" stroke="var(--icon-line)" stroke-width="1.5"/></svg>
        Vegan Friendly
      </div>
      <div class="claim claim-gelatin">
        <svg width="40" height="40" viewBox="0 0 40 40"><circle cx="20" cy="20" r="17" fill="none" stroke="var(--icon-line)" stroke-width="1.5"/><path d="M10 26 H30 M12 26 L14 14 H26 L28 26 M17 14 V26 M23 14 V26" fill="none" stroke="var(--icon-line)" stroke-width="1.5"/></svg>
        Gelatin Free
      </div>
    </section>

    <div class="count-badge">
      <span class="count-number">60</span>
      <span class="count-unit">Gummies</span>
    </div>

    <section class="benefits">
      <p class="benefits-heading">Blend for:</p>
      <ul class="benefits-list">
        <li><svg width="16" height="16" viewBox="0 0 16 16"><circle cx="8" cy="8" r="7" fill="var(--green)"/><path d="M4.5 8.2 L7 10.5 L11.5 5.5" fill="none" stroke="#fff" stroke-width="1.8"/></svg>Energy</li>
        <li><svg width="16" height="16" viewBox="0 0 16 16"><circle cx="8" cy="8" r="7" fill="var(--green)"/><path d="M4.5 8.2 L7 10.5 L11.5 5.5" fill="none" stroke="#fff" stroke-width="1.8"/></svg>Digestion</li>
        <li><svg width="16" height="16" viewBox="0 0 16 16"><circle cx="8" cy="8" r="7" fill="var(--green)"/><path d="M4.5 8.2 L7 10.5 L11.5 5.5" fill="none" stroke="#fff" stroke-width="1.8"/></svg>Immune Support*</li>
      </ul>
    </section>

    <div class="greens-art" role="img" aria-label="Photo of broccoli florets beside a wooden bowl of green superfood powder"></div>

    <footer class="footer-strip">
      <span class="footer-text">DIETARY SUPPLEMENT</span>
    </footer>
  </main>
</body>
</html>
```